New business logo / Business Card Design

My company provides Interim Management and consultancy, for Facilities Services. Covers any aspect of facilities management, including M&E, helpdesk, asset management, supplier relationships, catering, cleaning etc. Company provides innovative solutions to exceed client needs, drawing on years of experience. Initial thoughts on logo are attached below. Fits with RAG status on projects, red, amber and green, with logo design colours around moving services from amber to green.

Target Market(s)

Facilities Management clients and service providers

Industry/Entity Type

Business

Contact Information for Business Card

Company Name = k7Rventures Ltd My name on card = Derek Whitcombe, Director Mobile = 07516309842 Email = Derek@k7rventuresltd.co.uk Twitter = @k7Rventures Ltd

Font styles to use
Sans Serif

Colors
f37122
00a990

Requirements
Must have
• Logo to be evident, with some background image in reference to Facilities Management

```html
<!DOCTYPE html>
<html lang="en">
<head>
<meta charset="utf-8">
<title>k7Rventures Ltd – Business Card</title>
<link rel="stylesheet" href="https://fonts.googleapis.com/css2?family=Roboto:wght@400;500;700;900&display=swap">
<style>
  :root {
    --page-bg: #e9e6e1;
    --card-bg: #f7f8f9;
    --card-tint: #e8eef3;
    --brand-orange: #e0622b;
    --brand-green: #1e5a34;
    --ink: #1c1c1c;
    --ink-soft: #2e2e2e;
  }
  * { margin: 0; padding: 0; box-sizing: border-box; }
  html, body {
    width: 1200px; height: 970px; overflow: hidden;
    background: var(--page-bg);
    font-family: "Roboto", sans-serif;
  }
  .canvas { position: relative; width: 1200px; height: 970px; }
  .card {
    position: absolute; left: 105px; top: 160px;
    width: 990px; height: 649px;
    background: linear-gradient(160deg, var(--card-bg), var(--card-tint));
    box-shadow: 0 12px 36px rgba(0,0,0,0.18);
    overflow: hidden;
  }
  .card-shapes { position: absolute; inset: 0; width: 100%; height: 100%; }
  .brand {
    position: absolute; right: 77px; top: 122px; text-align: right;
  }
  .brand-mark {
    font-weight: 900; font-size: 58px; line-height: 1;
    color: var(--brand-green); letter-spacing: 0.5px;
  }
  .brand-company {
    margin-top: 8px;
    font-weight: 700; font-size: 45px; line-height: 1;
    color: var(--ink); letter-spacing: 0.5px;
  }
  .person { position: absolute; left: 73px; top: 330px; }
  .person-name {
    font-weight: 500; font-size: 43px; line-height: 1; color: var(--ink-soft);
  }
  .person-role {
    font-weight: 400; font-size: 31px; line-height: 1.05; color: var(--brand-orange);
  }
  .contacts {
    position: absolute; left: 73px; top: 458px; list-style: none;
  }
  .contact {
    display: flex; align-items: center; gap: 16px;
    height: 37px;
    font-size: 30px; font-weight: 400; color: var(--ink-soft);
  }
  .contact-icon {
    width: 30px; height: 30px; flex: none;
    background: var(--brand-green); border-radius: 2px;
    display: block;
  }
</style>
</head>
<body>
<main class="canvas">
  <section class="card" aria-label="Business card">
    <svg class="card-shapes" viewBox="0 0 900 590" preserveAspectRatio="none" aria-hidden="true">
      <defs>
        <linearGradient id="orange-sweep" x1="0" y1="0" x2="1" y2="0.4">
          <stop offset="0" stop-color="#e8703a"/>
          <stop offset="1" stop-color="#c9461b"/>
        </linearGradient>
        <linearGradient id="green-sweep" x1="1" y1="0" x2="0" y2="1">
          <stop offset="0" stop-color="#1f6138"/>
          <stop offset="1" stop-color="#0f3a1f"/>
        </linearGradient>
      </defs>
      <path class="swoosh-orange" fill="url(#orange-sweep)"
            d="M0,0 H900 V18 C650,12 420,40 260,105 C150,150 60,215 0,275 Z"/>
      <path class="swoosh-green" fill="url(#green-sweep)"
            d="M900,275 C820,400 600,525 0,548 V590 H900 Z"/>
      <path class="band-green" fill="#123f23"
            d="M0,552 C300,545 600,535 900,520 V590 H0 Z"/>
    </svg>

    <div class="brand">
      <div class="brand-mark">Northvale</div>
      <div class="brand-company">k7Rventures Ltd</div>
    </div>

    <div class="person">
      <div class="person-name">Derek Whitcombe</div>
      <div class="person-role">Director</div>
    </div>

    <ul class="contacts">
      <li class="contact">
        <svg class="contact-icon" viewBox="0 0 30 30" aria-hidden="true">
          <rect width="30" height="30" rx="2" fill="#1e5a34"/>
          <rect x="10" y="5" width="10" height="20" rx="2" fill="none" stroke="#fff" stroke-width="2"/>
          <rect x="12.5" y="8" width="5" height="6" fill="#fff"/>
        </svg>
        <span>07516309842</span>
      </li>
      <li class="contact">
        <svg class="contact-icon" viewBox="0 0 30 30" aria-hidden="true">
          <rect width="30" height="30" rx="2" fill="#1e5a34"/>
          <rect x="5" y="8" width="20" height="14" fill="none" stroke="#fff" stroke-width="2"/>
          <path d="M5,8 L15,17 L25,8 M5,22 L12,15 M25,22 L18,15" fill="none" stroke="#fff" stroke-width="2"/>
        </svg>
        <span>Derek@k7rventuresltd.co.uk</span>
      </li>
      <li class="contact">
        <span class="contact-icon" aria-hidden="true"></span>
        <span>@k7Rventures Ltd</span>
      </li>
    </ul>
  </section>
</main>
</body>
</html>
```